This is my scope and requirements:
Labelling project:
This is related to the Label project I also opened up. (The Brisk Owl Organic & Natural Soaps needs a good business card (Contest) )
I have attached an initial draft at a logo I tried to come up with for a business card and labelling/marketing. I am hoping that you can take this logo and 'run with it' to finesse it, make it look unique and professional. If you need to change it, I am open to ideas.
I find that labelling/packaging is hard for me to make it look 'professional' so I am coming to the experts!
I am looking for label designs for 2 different bottles and 2 different bar soaps:
1) Organic Bar Soap (2 possibilities: 1) Kraft 'cigar' band around soap with twine, 2) Kraft soap box with Kraft sticker Labels
2) Natural Olive Oil Based Bar Soap (labelling can be same as Organic but with distinct info)
3) Organic Hand Washes (clear square bottles, 250ml with natural pump)
4) Natural Olive Oil Based Body Wash (taper bottle 200ml with metal silver disc top caps)
I am a start up at home company making Organic and Natural Bar soaps, hand soaps, body washes.
All of my ingredients are organic or natural and will include natural essential oils, exfoliants, natural powders/colours, etc.
Some of the names are: Quillomé (feisty, energetic soap), Dunes (more of a sandalwood earthy tones with a sandalwood powder exfoliant), Frost (maybe changing this name - fresh scented), Amber Thyme (lemongrass/ginger, exfoliants), etc....
If you need more information, please let me know!
Please find attached: Kraft Paper I am looking at to possibly wrap the Bar Soaps in (I like the different colour concept and am trying to decide between diff colours of Ned Parrow paper to wrap around or plain kraft paper.. whichever the new logo concept will look best with.
The bottles I will be using for the hand soap (250ml square) and the body wash (200ml tapered)
OLD POST:
Hello! I am a start up business that is specializing in making luxury organic bar soaps, natural olive oil bar soaps, organic hand wash, natural olive oil body wash/shower gel that will include essential oils, exfoliants, natural powders, etc. (also accessories: wood soap dishes, etc) .. I am looking for a great designer that can provide me with the business card and labelling designs! I appreciate feedback, ideas on how I can receive a great design to help sell my products!
I am attaching my initial logo design that I would like to keep - but am looking for someone to 'finesse' it or make it more professional/unique looking.
Again, this is hand in hand with the business card project I submitted.
Thanks!
Verla
Updates
I am sorry for the lack of direction or Scope of the project. I am new at this board.
Labelling project:
I have attached an initial draft at a logo I tried to come up with for a business card and labelling/marketing. I am hoping that you can take this logo and 'run with it' to finesse it, make it look unique and professional.
If you need more information, please let me know.
Hello; I just wanted to let everyone know that if you feel that this brand needs a different logo, I am open to ideas (if you don't think the one I started with is ok). I am coming to the experts here!
Just to confirm also - this is related to the business card project, therefore, there are 2 projects, 2 payments! :)
Cheers
Industry/Entity Type
Business
Look and feel
Each slider illustrates characteristics of the customer's brand and the style your logo design should communicate.

```html
<!DOCTYPE html>
<html lang="en">
<head>
<meta charset="utf-8">
<title>The Brisk Owl – Quillomé Hand Wash Label</title>
<link rel="stylesheet" href="https://fonts.googleapis.com/css2?family=Delius&family=Special+Elite&display=swap">
<style>
  :root {
    --backdrop: #ecebe7;
    --label-sand: #e5dccf;
    --band-lilac: #c99ac6;
    --ink-grey: #807f82;
    --mark-grey: #939396;
    --paper-white: #ffffff;
    --faint-white: rgba(255, 255, 255, 0.55);
  }
  * { margin: 0; padding: 0; box-sizing: border-box; }
  html, body {
    width: 1200px;
    height: 1000px;
    overflow: hidden;
    background: var(--backdrop);
  }
  .label {
    position: absolute;
    left: 297px;
    top: 0;
    width: 605px;
    height: 1000px;
    background: var(--label-sand);
    overflow: hidden;
  }
  .lilac-band {
    position: absolute;
    left: 207px;
    top: 0;
    width: 188px;
    height: 700px;
    background: var(--band-lilac);
  }
  .side-motto {
    position: absolute;
    top: 500px;
    width: 1000px;
    font-family: "Delius", cursive;
    font-size: 33px;
    color: var(--faint-white);
    white-space: nowrap;
    text-align: center;
  }
  .side-motto--left {
    left: 58px;
    transform: translate(-50%, -50%) rotate(90deg);
  }
  .side-motto--right {
    left: 548px;
    transform: translate(-50%, -50%) rotate(-90deg);
  }
  .brand-mark {
    position: absolute;
    left: 80px;
    top: 70px;
    width: 445px;
    text-align: center;
    font-family: "Delius", cursive;
    color: var(--mark-grey);
  }
  .brand-mark__dot {
    width: 64px;
    height: 64px;
    margin: 0 auto 18px;
    border-radius: 50%;
    background: var(--mark-grey);
  }
  .brand-mark__name {
    font-size: 44px;
    line-height: 1.15;
  }
  .product-name {
    position: absolute;
    left: 0;
    top: 722px;
    width: 605px;
    text-align: center;
    font-family: "Delius", cursive;
    font-size: 52px;
    color: var(--ink-grey);
  }
  .product-tagline {
    position: absolute;
    left: 0;
    top: 786px;
    width: 605px;
    text-align: center;
    font-family: "Delius", cursive;
    font-size: 21px;
    color: var(--ink-grey);
  }
  .volume-panel {
    position: absolute;
    left: 207px;
    top: 838px;
    width: 188px;
    height: 162px;
    background: var(--band-lilac);
    display: flex;
    align-items: center;
    justify-content: center;
    text-align: center;
    font-family: "Special Elite", monospace;
    font-size: 21px;
    line-height: 1.45;
    color: var(--paper-white);
  }
</style>
</head>
<body>
  <main class="label">
    <div class="side-motto side-motto--left">100% organic earth friendly pure hand made</div>
    <div class="side-motto side-motto--right">100% organic earth friendly pure hand made</div>

    <div class="lilac-band"></div>

    <div class="brand-mark">
      <div class="brand-mark__dot"></div>
      <p class="brand-mark__name">The Brisk Owl Organic &amp; Natural Soaps</p>
    </div>

    <h1 class="product-name">Quillomé</h1>
    <p class="product-tagline">feisty, energetic soap</p>

    <div class="volume-panel">
      <p>250ML<br>ORGANIC<br>HAND WASH</p>
    </div>
  </main>
</body>
</html>
```